Harbinger Slabworks, Inc. Business Card

Create a business card that is eye catching and based around concrete sawcutting. I've attached our current business card and logo for reference. We like aspects of the current business card, but it is starting to feel very loud and lost. We would like something that is still fun but is more modern and streamlined.

```html
<!DOCTYPE html>
<html lang="en">
<head>
<meta charset="utf-8">
<title>Harbinger Slabworks, Inc. Business Card</title>
<link href="https://fonts.googleapis.com/css2?family=Montserrat:wght@400;500;700&display=swap" rel="stylesheet">
<style>
  :root {
    --backdrop: #e6e6e9;
    --card-white: #ffffff;
    --card-grey: #8e9096;
    --accent-red: #c8161d;
    --ink: #1e1e22;
    --navy: #1f2a6b;
  }
  * { box-sizing: border-box; margin: 0; padding: 0; }
  html, body { width: 1200px; height: 786px; overflow: hidden; }
  body {
    background: var(--backdrop);
    font-family: "Montserrat", sans-serif;
    display: flex;
    align-items: center;
    justify-content: center;
    gap: 48px;
  }
  .card {
    width: 520px;
    height: 298px;
    border-radius: 4px;
    box-shadow: 0 10px 28px rgba(0,0,0,.18);
    display: flex;
    align-items: center;
    position: relative;
  }
  .card--front { background: var(--card-white); }
  .card--back { background: var(--card-grey); }

  .brand-mark {
    width: 210px;
    display: flex;
    flex-direction: column;
    align-items: center;
    gap: 12px;
  }
  .brand-mark__dot {
    width: 74px; height: 74px;
    border-radius: 50%;
    background: var(--navy);
  }
  .brand-mark__name {
    font-weight: 700;
    font-size: 15px;
    line-height: 1.25;
    color: var(--navy);
    text-align: center;
    text-transform: uppercase;
    letter-spacing: .5px;
  }
  .card--back .brand-mark__name { color: var(--navy); }

  .divider {
    width: 2px;
    height: 168px;
    background: var(--accent-red);
    margin-right: 24px;
  }

  .details { color: var(--ink); }
  .details__name {
    color: var(--accent-red);
    font-weight: 700;
    font-size: 22px;
    margin-bottom: 12px;
  }
  .details__address {
    font-size: 13px;
    line-height: 1.35;
    margin-bottom: 12px;
  }
  .contact-list { list-style: none; font-size: 13px; }
  .contact-list li {
    display: flex; align-items: center; gap: 10px;
    margin-bottom: 7px;
  }
  .contact-list svg { width: 16px; height: 16px; flex: none; }

  .hotline {
    color: var(--accent-red);
    font-weight: 700;
    font-size: 18px;
    margin-bottom: 12px;
  }
  .service-list { list-style: none; font-size: 12px; font-weight: 500; color: var(--ink); text-transform: uppercase; }
  .service-list li { display: flex; align-items: center; gap: 7px; margin-bottom: 7px; }
  .service-list li::before {
    content: ""; width: 6px; height: 6px; border-radius: 50%;
    background: var(--accent-red);
  }
</style>
</head>
<body>
  <section class="card card--front">
    <div class="brand-mark">
      <span class="brand-mark__dot"></span>
      <span class="brand-mark__name">Harbinger<br>Slabworks, Inc.</span>
    </div>
    <div class="divider"></div>
    <div class="details">
      <h1 class="details__name">Marisa Delvecchio</h1>
      <p class="details__address">48 Kessler Ave<br>Ridgefield, NJ 07657</p>
      <ul class="contact-list">
        <li>
          <svg viewBox="0 0 16 16" aria-hidden="true"><path fill="#c8161d" d="M2 6c0-2 2-3 6-3s6 1 6 3v1h-3V6H5v1H2zM4 8h8l1 5H3z"/><circle cx="8" cy="10.5" r="1.4" fill="#fff"/></svg>
          855.555.0142
        </li>
        <li>
          <svg viewBox="0 0 16 16" aria-hidden="true"><rect x="4" y="1" width="8" height="14" rx="1.5" fill="none" stroke="#c8161d" stroke-width="1.6"/><circle cx="8" cy="12.3" r=".9" fill="#c8161d"/></svg>
          973.555.0187
        </li>
        <li>
          <svg viewBox="0 0 16 16" aria-hidden="true"><rect x="1" y="3.5" width="14" height="9" fill="#c8161d"/><path d="M1 3.5l7 5 7-5" fill="none" stroke="#fff" stroke-width="1.2"/></svg>
          marisa@harbingerslab.com
        </li>
      </ul>
    </div>
  </section>

  <section class="card card--back">
    <div class="brand-mark">
      <span class="brand-mark__dot"></span>
      <span class="brand-mark__name">Harbinger<br>Slabworks, Inc.</span>
    </div>
    <div class="divider"></div>
    <div class="details">
      <p class="hotline">855-SLABCUT</p>
      <ul class="service-list">
        <li>Wall Sawing</li>
        <li>Core Drilling</li>
        <li>Slab Sawing</li>
        <li>Breaking &amp; Removal</li>
      </ul>
    </div>
  </section>
</body>
</html>
```